RM Tomás Rivera (Business Card)

Hi designers, in this work, I'm looking for an sophisticated stylish, elegant and proffesional personal card. We have a laboratory of pathology automated, with equipments high quality.
In this web the designers, have created my business logo, the name is "RM Tomás Rivera"
In our lab, we principal work is to prepare the biopsies for further diagnostic of diseases like cancer, tumors, etc.
I need that the first face, only having my complete logo (Rm Tomás Rivera, Laboratorio de procesamiento Histologico)
The overleaf, could repeat the same logo, like water logo.
In this face, I need to say: My full data:

Técnico en Anatomía Patológica
Tomás Rivera Ibarra M.P 47203
Av. Paredes Luján 418 - 2do piso - Instituto Marbel.
Córdoba, Argentina
(0351) 154820937
rivera.tomas@correolab.example

with respect the colors of card, use your imagination, the original logo color is violet, I haven't chosen a color base for the card.

attached pictures are examples of cards I like your DESIGN.
Attached too, the original logo to my company.

the size of card are:
horizontal: 9cm
vertical: 5,5cm

any question that you have, not doubt to question me,
Hand to work!

Industry/Entity Type

Laboratory

Requirements
Must have
• designers sophisticated, not simples, like show the images attached

```html
<!DOCTYPE html>
<html lang="es">
<head>
<meta charset="utf-8">
<title>RM Tomás Rivera – Tarjeta personal</title>
<link rel="stylesheet" href="https://fonts.googleapis.com/css2?family=Questrial&family=Roboto+Condensed:wght@400;700&display=swap">
<style>
  :root {
    --backdrop: #2e2420;
    --card-white: #ffffff;
    --card-shade: #e6e6e8;
    --violet: #5b2a86;
    --violet-deep: #4a1f72;
    --violet-faint: rgba(255, 255, 255, 0.10);
    --ink-grey: #6b6b6e;
    --ink-soft: #8d8d90;
    --rule-grey: #c9c9cc;
  }
  * { box-sizing: border-box; margin: 0; padding: 0; }
  html, body { width: 1200px; height: 900px; overflow: hidden; }
  body {
    background: var(--backdrop);
    font-family: "Questrial", sans-serif;
    display: flex;
    flex-direction: column;
    align-items: center;
    justify-content: center;
    gap: 40px;
  }
  .card {
    position: relative;
    width: 640px;
    height: 391px;
    border-radius: 22px;
    overflow: hidden;
    background: linear-gradient(160deg, var(--card-white) 30%, var(--card-shade) 100%);
  }
  .card-curves { position: absolute; inset: 0; width: 100%; height: 100%; }
  .brand {
    position: absolute;
    display: flex;
    flex-direction: column;
    align-items: center;
  }
  .brand-row { display: flex; align-items: center; gap: 12px; }
  .brand-square { width: 22px; height: 22px; background: var(--violet); }
  .brand-name {
    font-family: "Questrial", sans-serif;
    font-size: 30px;
    color: var(--ink-grey);
    letter-spacing: 4px;
  }
  .brand-lab {
    margin-top: 6px;
    padding-top: 5px;
    border-top: 1px solid var(--ink-grey);
    font-family: "Roboto Condensed", sans-serif;
    font-weight: 700;
    font-size: 17px;
    color: var(--ink-grey);
    text-transform: uppercase;
    letter-spacing: 0.3px;
  }
  .front .brand { left: 70px; top: 92px; }
  .front-watermark {
    position: absolute;
    right: 90px;
    bottom: 92px;
    font-size: 30px;
    letter-spacing: 4px;
    color: var(--violet-faint);
  }
  .back .brand { left: 0; right: 0; top: 38px; }
  .back .brand-name { font-size: 26px; }
  .back .brand-lab { font-size: 15px; }
  .address {
    position: absolute;
    left: 0; right: 0; top: 128px;
    text-align: center;
    font-size: 9.5px;
    line-height: 1.45;
    color: var(--ink-soft);
  }
  .holder { position: absolute; left: 50px; top: 218px; }
  .holder-name { font-size: 22px; color: var(--ink-grey); letter-spacing: 0.5px; }
  .holder-role, .holder-reg { font-size: 13px; color: var(--violet); margin-top: 3px; }
  .holder-reg { padding-left: 86px; }
  .divider {
    position: absolute;
    left: 352px; top: 170px;
    width: 2px; height: 70px;
    background: linear-gradient(var(--violet), transparent);
  }
  .contact {
    position: absolute;
    left: 380px; top: 178px;
    font-size: 12px;
    line-height: 2.2;
    color: var(--ink-grey);
  }
</style>
</head>
<body>

  <section class="card front" aria-label="Frente de la tarjeta">
    <svg class="card-curves" viewBox="0 0 640 391" preserveAspectRatio="none" aria-hidden="true">
      <path d="M0,352 C190,262 410,164 640,118" fill="none" stroke="var(--rule-grey)" stroke-width="3"/>
      <path d="M0,391 L0,372 C200,282 420,186 640,142 L640,391 Z" fill="var(--violet)"/>
    </svg>
    <div class="brand">
      <div class="brand-row">
        <span class="brand-square"></span>
        <span class="brand-name">RM Tomás Rivera</span>
      </div>
      <div class="brand-lab">Laboratorio de Procesamiento Histológico</div>
    </div>
    <div class="front-watermark" aria-hidden="true">RM Tomás Rivera</div>
  </section>

  <section class="card back" aria-label="Dorso de la tarjeta">
    <svg class="card-curves" viewBox="0 0 640 391" preserveAspectRatio="none" aria-hidden="true">
      <path d="M0,325 C220,318 450,286 640,238" fill="none" stroke="var(--rule-grey)" stroke-width="3"/>
      <path d="M0,391 L0,345 C220,338 450,306 640,258 L640,391 Z" fill="var(--violet)"/>
    </svg>
    <div class="brand">
      <div class="brand-row">
        <span class="brand-square"></span>
        <span class="brand-name">RM Tomás Rivera</span>
      </div>
      <div class="brand-lab">Laboratorio de Procesamiento Histológico</div>
    </div>
    <p class="address">Av. Paredes Luján 418 - 2do piso - Instituto Marbel.<br>Córdoba, Argentina</p>
    <div class="holder">
      <p class="holder-name">Tomás Rivera Ibarra</p>
      <p class="holder-role">Técnico en Anatomía Patológica</p>
      <p class="holder-reg">M.P 47203</p>
    </div>
    <span class="divider" aria-hidden="true"></span>
    <div class="contact">
      <p>P: (0351) 154820937</p>
      <p>E: rivera.tomas@correolab.example</p>
    </div>
  </section>

</body>
</html>
```